依頼概要
■依頼の目的/概要
弊社が販売を予定しているオリジナルサイダーのラベルデザインをお願いします。
■依頼詳細
今回は弊社が販売する吟醸香がするオリジナルサイダーラベルのデザインをお願いします。
商品名は雲雀野サイダーです。

■その他要望
イメージは昭和レトロなサイダー感で、それでいて店頭で目に付くデザイン。
仕込み水を使用したサイダーなのでその表記も入れる。
商品名は雲雀野サイダーです。
添付資料は弊社のロゴです、使っても使わなくてもどちらでも結構です。

その他何かご不明な点がございましたら、お気軽にご質問下さい。
よろしくお願いいたします。

```html
<!DOCTYPE html>
<html lang="ja">
<head>
<meta charset="utf-8">
<title>雲雀野サイダー ラベル</title>
<link href="https://fonts.googleapis.com/css2?family=Zen+Maru+Gothic:wght@500;700;900&display=swap" rel="stylesheet">
<style>
  :root {
    --teal: #3a86a3;
    --teal-dark: #2c6f88;
    --gold: #d9a441;
    --gold-soft: #ecd39c;
    --cream: #f7efd9;
    --paper: #ffffff;
  }
  html, body {
    margin: 0;
    padding: 0;
    width: 792px;
    height: 1200px;
    overflow: hidden;
    background: var(--paper);
  }
  .label {
    display: block;
    width: 792px;
    height: 1200px;
    font-family: "Zen Maru Gothic", sans-serif;
  }
  .label-body { fill: var(--cream); stroke: var(--teal); stroke-width: 7; }
  .label-inner { fill: none; stroke: var(--teal); stroke-width: 2.5; }
  .brand-circle { fill: var(--cream); stroke: var(--teal); stroke-width: 5; }
  .brand-name { fill: var(--teal); font-weight: 700; font-size: 40px; }
  .arch-text { fill: var(--teal); font-weight: 500; font-size: 44px; letter-spacing: 3px; }
  .title-main { fill: var(--teal); font-weight: 900; font-size: 104px; letter-spacing: 4px; }
  .title-sub { fill: var(--gold); font-weight: 900; font-size: 80px; letter-spacing: 2px; }
  .tagline { fill: var(--teal); font-weight: 900; font-size: 62px; }
  .ribbon-band { fill: var(--cream); stroke: var(--teal); stroke-width: 4; stroke-linejoin: round; }
  .ribbon-fold { fill: var(--gold-soft); stroke: var(--teal); stroke-width: 4; stroke-linejoin: round; }
  .ribbon-text { fill: var(--teal); font-weight: 700; font-size: 46px; letter-spacing: 3px; }
</style>
</head>
<body>
<svg class="label" viewBox="0 0 792 1200" xmlns="http://www.w3.org/2000/svg">
  <defs>
    <linearGradient id="illustrationTone" x1="0" y1="0" x2="0" y2="1">
      <stop offset="0" stop-color="#f3e3bd"/>
      <stop offset="1" stop-color="#ead2a0"/>
    </linearGradient>
    <clipPath id="innerClip">
      <path d="M110,1010 V350 C110,250 230,205 396,205 C562,205 682,250 682,350 V1010 Q682,1038 654,1038 H138 Q110,1038 110,1010 Z"/>
    </clipPath>
    <path id="archPath" d="M150,420 C150,260 270,240 396,240 C522,240 642,260 642,420"/>
  </defs>

  <!-- label shape -->
  <path class="label-body" d="M92,1020 V345 C92,225 220,180 396,180 C572,180 700,225 700,345 V1020 Q700,1056 664,1056 H128 Q92,1056 92,1020 Z"/>
  <path class="label-inner" d="M110,1010 V350 C110,250 230,205 396,205 C562,205 682,250 682,350 V1010 Q682,1038 654,1038 H138 Q110,1038 110,1010 Z"/>

  <!-- brand emblem -->
  <circle class="brand-circle" cx="396" cy="198" r="76"/>
  <text class="brand-name" x="396" y="212" text-anchor="middle">雲雀野</text>

  <!-- arched wordmark -->
  <text class="arch-text">
    <textPath href="#archPath" startOffset="2%">hibari</textPath>
  </text>
  <text class="arch-text">
    <textPath href="#archPath" startOffset="98%" text-anchor="end">cider</textPath>
  </text>

  <!-- product name -->
  <text class="title-main" x="396" y="458" text-anchor="middle">雲雀野</text>
  <text class="title-sub" x="396" y="548" text-anchor="middle">サイダー</text>

  <!-- illustration field -->
  <g clip-path="url(#innerClip)">
    <rect x="110" y="590" width="572" height="420" fill="url(#illustrationTone)"
          role="img" aria-label="麻の葉模様の背景に描かれた力士のイラスト"/>
  </g>

  <!-- tagline -->
  <text class="tagline" transform="translate(300 690) rotate(-12)" text-anchor="middle">
    <tspan x="0" dy="0">う</tspan><tspan x="6" dy="64">ま</tspan><tspan x="12" dy="64">い</tspan><tspan x="18" dy="58">!</tspan>
  </text>

  <!-- ribbon -->
  <g class="ribbon">
    <path class="ribbon-fold" d="M200,905 L150,905 L172,940 L150,975 L220,975 Z"/>
    <path class="ribbon-fold" d="M592,905 L642,905 L620,940 L642,975 L572,975 Z"/>
    <path class="ribbon-band" d="M200,880 Q396,860 592,880 L592,950 Q396,930 200,950 Z"/>
    <text class="ribbon-text" x="396" y="932" text-anchor="middle">仕込み水使用</text>
  </g>
</svg>
</body>
</html>
```